依頼詳細
シンプルというよりは、見やすくスッキリとしたデザインで目にとまるようなデザインにしたいです。

・角2封筒 表フルカラー
縦向き、郵便番号枠不要、住所記入線不要

・長3封筒 表フルカラー
横向き、郵便番号枠不要、住所記入線をお願いします。

インクモールへ印刷発注の為、専用テンプレートを使用し、そのままインクモールで印刷依頼が可能な仕様のデータで納品をお願いします。
デザインの印刷範囲制限がありますので、範囲内でお願いします。

封筒の色ですが、インクモールで封筒のサンプルを取り寄せ確認したところ、
クリニックのロゴが木のため、ペールノビア、ミルドトーンリーフがいいのではと考えております。
記載項目
記載項目などは添付ファイルをご参照ください。
希望イメージ
シンプル 複雑
単色 カラフル
暗い 明るい
日常 高級
遊び心 厳粛
未来的 伝統的
女性的 男性的
希望する色
納品ファイル
• 高解像度JPG (.jpg)
• イラストレーター形式 (.ai)
補足説明
添付したロゴを使用してください。
■ 選んだ理由

とてもきれいなデザインで気に入りました。

■ 提案者全員のお礼・コメント

素敵なデザインが多く迷いました。
たくさんのご提案ありがとうございます。

```html
<!DOCTYPE html>
<html lang="ja">
<head>
<meta charset="utf-8">
<title>封筒デザイン 角2・長3</title>
<link href="https://fonts.googleapis.com/css2?family=Noto+Sans+JP:wght@400;500;700&display=swap" rel="stylesheet">
<style>
  :root{
    --bg:#e3e3e3;
    --paper:#ffffff;
    --paper-edge:#d2d2d2;
    --flap-shade:#f4f4f4;
    --ink:#333333;
    --leaf:#6a9a3c;
    --muted:#777777;
    --rule:#cfcfcf;
    --label:#8a8a8a;
  }
  *{margin:0;padding:0;box-sizing:border-box;}
  html,body{width:1200px;height:2392px;overflow:hidden;background:var(--bg);}
  body{position:relative;font-family:"Noto Sans JP",sans-serif;color:var(--ink);}
  .sheet-label{position:absolute;font-size:22px;color:var(--label);letter-spacing:.05em;}
  .label-kaku2{top:26px;right:40px;}
  .label-naga3{top:2030px;right:100px;}
  .envelopes{position:absolute;inset:0;}
  .brand{position:absolute;display:flex;align-items:center;}
  .brand-mark{border-radius:50%;background:var(--leaf);flex:none;}
  .brand-text{display:flex;flex-direction:column;}
  .brand-corp{color:var(--ink);font-weight:500;}
  .brand-name{color:var(--ink);font-weight:700;letter-spacing:.04em;line-height:1.1;}
  .brand-en{color:var(--leaf);font-weight:500;letter-spacing:.04em;}
  .divider{position:absolute;width:2px;background:var(--rule);}
  .contact{position:absolute;color:var(--muted);}
  .contact p{white-space:nowrap;}
  /* 角2 */
  .kaku2 .brand{left:140px;top:1430px;gap:18px;}
  .kaku2 .brand-mark{width:76px;height:76px;}
  .kaku2 .brand-corp{font-size:18px;}
  .kaku2 .brand-name{font-size:40px;}
  .kaku2 .brand-en{font-size:17px;margin-top:4px;}
  .kaku2 .divider{left:528px;top:1432px;height:108px;}
  .kaku2 .contact{left:548px;top:1436px;font-size:14px;line-height:32px;}
  /* 長3 */
  .naga3 .brand{left:148px;top:2282px;gap:9px;}
  .naga3 .brand-mark{width:38px;height:38px;}
  .naga3 .brand-corp{font-size:10px;}
  .naga3 .brand-name{font-size:20px;}
  .naga3 .brand-en{font-size:9px;margin-top:2px;}
  .naga3 .divider{left:362px;top:2282px;height:52px;width:1px;}
  .naga3 .contact{left:374px;top:2282px;font-size:9px;line-height:17px;}
</style>
</head>
<body>
  <div class="sheet-label label-kaku2">角２封筒デザインA</div>
  <div class="sheet-label label-naga3">長３封筒デザイン（共通）</div>

  <svg class="envelopes" width="1200" height="2392" viewBox="0 0 1200 2392" aria-hidden="true">
    <!-- 角2: flap and body -->
    <path d="M120 120 L150 72 L1050 72 L1080 120 Z" fill="var(--flap-shade)" stroke="var(--paper-edge)" stroke-width="2"/>
    <rect x="120" y="120" width="960" height="1820" fill="var(--paper)" stroke="var(--paper-edge)" stroke-width="2"/>
    <line x1="120" y1="200" x2="1080" y2="200" stroke="#ececec" stroke-width="2"/>
    <!-- 長3: body and side flap -->
    <path d="M980 2080 L1088 2110 L1088 2330 L980 2360 Z" fill="var(--flap-shade)" stroke="var(--paper-edge)" stroke-width="2"/>
    <rect x="128" y="2080" width="852" height="280" fill="var(--paper)" stroke="var(--paper-edge)" stroke-width="2"/>
    <!-- 長3 address lines -->
    <line x1="312" y1="2148" x2="940" y2="2148" stroke="var(--rule)" stroke-width="2"/>
    <line x1="312" y1="2208" x2="940" y2="2208" stroke="var(--rule)" stroke-width="2"/>
    <line x1="312" y1="2268" x2="940" y2="2268" stroke="var(--rule)" stroke-width="2"/>
  </svg>

  <section class="kaku2">
    <div class="brand">
      <span class="brand-mark"></span>
      <div class="brand-text">
        <span class="brand-corp">医療法人</span>
        <span class="brand-name">さくらだ眼科</span>
        <span class="brand-en">Sakurada Eye Clinic</span>
      </div>
    </div>
    <div class="divider"></div>
    <div class="contact">
      <p>〒000-0000 大阪府架空市中央町1-2-3</p>
      <p>TEL 00-0000-0000</p>
      <p>info@sakurada-eye.jp</p>
    </div>
  </section>

  <section class="naga3">
    <div class="brand">
      <span class="brand-mark"></span>
      <div class="brand-text">
        <span class="brand-corp">医療法人</span>
        <span class="brand-name">さくらだ眼科</span>
        <span class="brand-en">Sakurada Eye Clinic</span>
      </div>
    </div>
    <div class="divider"></div>
    <div class="contact">
      <p>〒000-0000 大阪府架空市中央町1-2-3</p>
      <p>TEL 00-0000-0000</p>
      <p>info@sakurada-eye.jp</p>
    </div>
  </section>
</body>
</html>
```